4R Capital business cards for a tech VC

We're starting a new Venture Capital that is focusing on bringing the best start ups from Israel to NYC
We need a business cards template for this that gives the sense of an entrepreneurial look
I don't want any religious signs on this even thought it's Israel
I'm looking for a techi feeling but not too crazy
The card should probably be in the same light blue as the logo and the logo in white

Target Market(s)

Investors

Industry/Entity Type

Tech

Contact Information for Business Card

The card needs to look slick and entrepreneurship like
The VC is focused on NYC and Tel Aviv so could be great to show something on the back side that is like NYC skyline or something like that
You can see the logo attached

Colors
0455a3
3276b5
85acd3
cedeed
eaf1f7

Requirements
Must have
• A very cool looking business card that shows we're a cutting edge tech VC with a focus on bringing start ups from Tel Aviv and leveraging the NYC ecosystem
Nice to have
• NYC skyline can be cool , maybe something that is connected to Tel Aviv

```html
<!DOCTYPE html>
<html lang="en">
<head>
<meta charset="utf-8">
<title>4R Capital Business Cards</title>
<link href="https://fonts.googleapis.com/css2?family=Dosis:wght@400;500;600&display=swap" rel="stylesheet">
<style>
  :root {
    --brand-deep: #0455a3;
    --brand-mid: #3276b5;
    --brand-sky: #2b8ad0;
    --brand-soft: #85acd3;
    --brand-pale: #cedeed;
    --brand-mist: #eaf1f7;
    --paper: #ffffff;
    --backdrop: #e4e7eb;
  }
  * { box-sizing: border-box; margin: 0; padding: 0; }
  html, body { width: 1200px; height: 873px; overflow: hidden; }
  body {
    background: var(--backdrop);
    font-family: "Dosis", sans-serif;
    display: flex;
    align-items: center;
    justify-content: center;
    gap: 60px;
  }
  .card {
    position: relative;
    width: 520px;
    height: 300px;
    background: var(--paper);
    overflow: hidden;
    box-shadow: 0 10px 30px rgba(0,0,0,0.18);
  }
  .brand {
    position: absolute;
    display: flex;
    align-items: center;
    gap: 10px;
    color: var(--brand-deep);
    font-weight: 500;
    white-space: nowrap;
  }
  .brand-mark { background: var(--brand-sky); flex: none; border-radius: 50%; }

  /* Contact side */
  .contact-card .brand { top: 38px; left: 250px; font-size: 26px; }
  .contact-card .brand-mark { width: 16px; height: 16px; }
  .contact-panel {
    position: absolute;
    left: 0; right: 0; bottom: 0;
    height: 175px;
    background: var(--brand-sky);
  }
  .skyline {
    position: absolute;
    left: 0; top: 60px;
    width: 220px; height: 70px;
    background: linear-gradient(180deg, var(--brand-mid), var(--brand-sky));
  }
  .holder {
    position: absolute;
    left: 250px; top: 132px;
    color: var(--paper);
  }
  .holder-name { font-size: 26px; font-weight: 500; letter-spacing: 0.04em; line-height: 1; }
  .holder-role { font-size: 12px; margin-top: 2px; }
  .holder-rule {
    position: absolute;
    left: 250px; right: 30px; top: 178px;
    height: 1px; background: var(--paper);
  }
  .contact-list {
    position: absolute;
    left: 250px; top: 190px;
    list-style: none;
    color: var(--paper);
    font-size: 14px;
    line-height: 20px;
  }
  .contact-list li { display: flex; align-items: center; gap: 8px; }
  .contact-list svg { width: 12px; height: 12px; flex: none; }

  /* Logo side */
  .logo-card .brand { top: 108px; left: 0; right: 0; justify-content: center; font-size: 38px; }
  .logo-card .brand-mark { width: 22px; height: 22px; }
  .logo-card .accent-band {
    position: absolute; left: 0; bottom: 0;
    width: 100%; height: 70px;
  }
</style>
</head>
<body>

<section class="card contact-card">
  <div class="brand"><span class="brand-mark"></span>4R Capital</div>
  <div class="skyline" role="img" aria-label="New York City skyline silhouette"></div>
  <div class="contact-panel"></div>
  <div class="holder">
    <p class="holder-name">DANA LEVIN</p>
    <p class="holder-role">manager</p>
  </div>
  <div class="holder-rule"></div>
  <ul class="contact-list">
    <li><svg viewBox="0 0 12 12"><circle cx="6" cy="6" r="6" fill="#fff"/><path d="M4 3.5l1 1-0.6 0.8a3 3 0 0 0 1.3 1.3l0.8-0.6 1 1-0.7 0.8C5.3 7.6 4.4 6.7 3.2 4.2z" fill="#2b8ad0"/></svg>+1 212 555 0147</li>
    <li><svg viewBox="0 0 12 12"><circle cx="6" cy="6" r="6" fill="#fff"/><rect x="3" y="4" width="6" height="4" fill="none" stroke="#2b8ad0"/><path d="M3 4l3 2 3-2" fill="none" stroke="#2b8ad0"/></svg>dana@4rfund.com</li>
    <li><svg viewBox="0 0 12 12"><circle cx="6" cy="6" r="6" fill="#fff"/><circle cx="6" cy="6" r="3" fill="none" stroke="#2b8ad0"/><path d="M3 6h6" stroke="#2b8ad0"/></svg>www.4rfund.com</li>
    <li><svg viewBox="0 0 12 12"><circle cx="6" cy="6" r="6" fill="#fff"/><path d="M6 9.5L4 6a2 2 0 1 1 4 0z" fill="#2b8ad0"/></svg>88 Harbor Ave. your City, State, Zip</li>
  </ul>
</section>

<section class="card logo-card">
  <div class="brand"><span class="brand-mark"></span>4R Capital</div>
  <svg class="accent-band" viewBox="0 0 520 70" preserveAspectRatio="none">
    <rect x="0" y="0" width="520" height="70" fill="#2b8ad0"/>
    <polygon points="0,0 120,0 90,70 0,70" fill="#3276b5"/>
    <polygon points="400,0 520,0 520,70 430,70" fill="#5aa3dc"/>
  </svg>
</section>

</body>
</html>
```